I am looking for a modern style design for a podcast cover art.
Titled: Open Horizon with R.T. Pellow
colors to stay in the grays, reds, blacks, white, gold, and maybe blues if it fits well. I attached a mock up of what we are going for and a current podcast cover we drew inspiration from.
Colors
3276b5
ec1f27
f04a50
1b1b1b
474747
919191
d2d2d2

```html
<!DOCTYPE html>
<html lang="en">
<head>
<meta charset="utf-8">
<title>Open Horizon with R.T. Pellow</title>
<link rel="stylesheet" href="https://fonts.googleapis.com/css2?family=Josefin+Sans:wght@300&family=Montserrat:wght@800&family=Marcellus&display=swap">
<style>
  :root {
    --bg-top: #3a302a;
    --bg-mid: #8f8378;
    --bg-low: #e8e2da;
    --panel-edge: #ffffff;
    --red: #ec1f27;
    --red-soft: #f04a50;
    --black: #1b1b1b;
    --charcoal: #474747;
    --gray: #919191;
    --silver: #d2d2d2;
    --blue: #3276b5;
    --gold: #e9b24a;
    --text: #ffffff;
  }
  html, body {
    margin: 0;
    padding: 0;
    width: 1200px;
    height: 1200px;
    overflow: hidden;
  }
  .cover {
    position: relative;
    width: 1200px;
    height: 1200px;
    overflow: hidden;
    background: linear-gradient(180deg, var(--bg-top) 0%, var(--bg-mid) 30%, var(--bg-low) 70%, #f4f0ea 100%);
  }
  .strip {
    position: absolute;
    border: 8px solid var(--panel-edge);
    box-shadow: 0 10px 30px rgba(0,0,0,0.4);
  }
  .strip--red    { left: -60px;  top: 80px; width: 120px; height: 1180px; background: linear-gradient(180deg, #c9121d, var(--red) 50%, var(--red-soft)); transform: rotate(1deg); }
  .strip--gray   { left: 78px;   top: 36px; width: 290px; height: 1120px; background: linear-gradient(180deg, var(--charcoal), var(--gray) 55%, #a9a9a9); transform: rotate(0.6deg); }
  .strip--blue   { left: 318px;  top: 82px; width: 270px; height: 1150px; background: linear-gradient(180deg, #245a8c, var(--blue) 50%, #5c95c9); transform: rotate(1.2deg); }
  .strip--silver { left: 572px;  top: 44px; width: 228px; height: 1150px; background: linear-gradient(180deg, #bdbdbd, var(--silver) 40%, #eeeeee); transform: rotate(1.4deg); }
  .strip--gold   { left: 792px;  top: 72px; width: 270px; height: 1130px; background: linear-gradient(180deg, var(--gold), #f0c766 45%, #f5e0a8); transform: rotate(0.4deg); }
  .strip--coral  { left: 1040px; top: 86px; width: 220px; height: 1150px; background: linear-gradient(180deg, var(--red-soft), #e4645e 50%, #c7282e); transform: rotate(2.4deg); }

  .host-photo {
    position: absolute;
    left: 800px;
    top: 290px;
    width: 400px;
    height: 910px;
    background: linear-gradient(90deg, #9a7440 0%, #a8452f 45%, #8e1f1c 100%);
  }

  .title-small {
    position: absolute;
    left: 118px;
    top: 360px;
    margin: 0;
    font-family: "Josefin Sans", sans-serif;
    font-weight: 300;
    font-size: 150px;
    line-height: 1;
    color: var(--text);
    text-shadow: 0 4px 14px rgba(0,0,0,0.25);
  }
  .title-big {
    position: absolute;
    left: 140px;
    top: 700px;
    margin: 0;
    font-family: "Montserrat", sans-serif;
    font-weight: 800;
    font-size: 168px;
    letter-spacing: -2px;
    line-height: 1;
    color: var(--text);
    text-shadow: 0 6px 18px rgba(0,0,0,0.35);
  }
  .host-name {
    position: absolute;
    right: 36px;
    top: 1082px;
    margin: 0;
    font-family: "Marcellus", serif;
    font-size: 76px;
    letter-spacing: 3px;
    line-height: 1;
    color: var(--text);
    text-shadow: 0 3px 10px rgba(0,0,0,0.3);
  }
</style>
</head>
<body>
<main class="cover">
  <div class="strip strip--red"></div>
  <div class="strip strip--gray"></div>
  <div class="strip strip--blue"></div>
  <div class="strip strip--silver"></div>
  <div class="strip strip--gold"></div>
  <div class="strip strip--coral"></div>

  <div class="host-photo" role="img" aria-label="Photo of the host in a tuxedo and bow tie, pointing toward the title"></div>

  <h1 class="title-small">OPEN</h1>
  <h2 class="title-big">HORIZON</h2>
  <p class="host-name">WITH R.T. PELLOW</p>
</main>
</body>
</html>
```